Complete Banner Set For Web Display Ads - Including Zimbly

Ads are driving to a free web class on real estate investing made easy. The offer is for software and training that solves their number 1 challenge - Finding Deals.
Examples of copy suggestions and offer....
"Invest In Real Estate Like A Pro"
"Access Never Before Seen Inventory In Seconds"
"The Country's Best Source For Off-Market Deals"
Brody Halvaney "#1 Real Estate Investing Strategy"
Real Estate

```html
<!DOCTYPE html>
<html lang="en">
<head>
<meta charset="utf-8">
<title>Invest In Real Estate Like A Pro</title>
<link href="https://fonts.googleapis.com/css2?family=Oswald:wght@400;500;700&display=swap" rel="stylesheet">
<style>
  :root {
    --slate: #3a4551;
    --orange: #f7941d;
    --green: #8dc63f;
    --white: #ffffff;
    --rule: #6d7783;
    --button-ink: #2f3b46;
    --photo-light: #e9e7e3;
    --photo-mid: #b9b6b1;
    --photo-dark: #6c6a68;
  }
  html, body {
    margin: 0;
    padding: 0;
    width: 1200px;
    height: 948px;
    overflow: hidden;
    background: var(--slate);
  }
  .banner {
    position: relative;
    width: 1200px;
    height: 948px;
    overflow: hidden;
    font-family: "Oswald", "Arial Narrow", sans-serif;
  }
  .banner__photo {
    position: absolute;
    top: 0;
    left: 560px;
    width: 640px;
    height: 948px;
    background:
      linear-gradient(180deg, rgba(255,255,255,0.35) 0%, rgba(0,0,0,0) 40%, rgba(0,0,0,0.15) 100%),
      linear-gradient(90deg, var(--photo-mid) 0%, var(--photo-light) 35%, var(--photo-light) 55%, var(--photo-dark) 78%, var(--photo-mid) 100%);
  }
  .banner__panel {
    position: absolute;
    top: 0;
    left: 0;
    width: 920px;
    height: 948px;
    background: linear-gradient(90deg, var(--slate) 0%, var(--slate) 78%, rgba(58,69,81,0.7) 88%, rgba(58,69,81,0) 100%);
  }
  .headline {
    position: absolute;
    left: 50px;
    top: 22px;
    margin: 0;
    font-weight: 700;
    text-transform: uppercase;
    line-height: 1;
  }
  .headline__line { display: block; white-space: nowrap; }
  .headline__line--orange { color: var(--orange); font-size: 116px; line-height: 128px; }
  .headline__line--green { color: var(--green); font-size: 162px; line-height: 148px; letter-spacing: -1px; }
  .headline__line--pro { color: var(--orange); font-size: 112px; line-height: 124px; }
  .divider {
    position: absolute;
    left: 52px;
    top: 444px;
    width: 644px;
    height: 2px;
    background: var(--rule);
  }
  .benefits {
    position: absolute;
    left: 52px;
    top: 470px;
    margin: 0;
    padding: 0;
    list-style: none;
    color: var(--white);
    font-weight: 500;
    font-size: 50px;
    line-height: 60px;
    letter-spacing: 2px;
  }
  .benefits__item {
    position: relative;
    padding-left: 48px;
    margin-bottom: 30px;
    white-space: nowrap;
  }
  .benefits__item::before {
    content: "";
    position: absolute;
    left: 4px;
    top: 26px;
    width: 14px;
    height: 14px;
    border-radius: 50%;
    background: var(--white);
  }
  .cta {
    position: absolute;
    left: 840px;
    top: 868px;
    width: 198px;
    height: 64px;
    border-radius: 32px;
    background: var(--green);
    color: var(--button-ink);
    font-weight: 400;
    font-size: 30px;
    line-height: 1;
    white-space: nowrap;
    display: flex;
    align-items: center;
    justify-content: center;
    gap: 10px;
    box-sizing: border-box;
  }
  .cta__icon { width: 32px; height: 32px; flex: none; }
</style>
</head>
<body>
  <div class="banner">
    <div class="banner__photo" role="img" aria-label="Photo of a bald, bearded man in a grey suit sitting on outdoor concrete stairs"></div>
    <div class="banner__panel"></div>

    <h1 class="headline">
      <span class="headline__line headline__line--orange">Invest In</span>
      <span class="headline__line headline__line--green">Real Estate</span>
      <span class="headline__line headline__line--pro">Like A Pro</span>
    </h1>

    <div class="divider"></div>

    <ul class="benefits">
      <li class="benefits__item">Access Never Before Seen<br>Inventory In Seconds</li>
      <li class="benefits__item">The Country's Best Source<br>For Off-Market Deals</li>
      <li class="benefits__item">Brody Halvaney "#1 Real<br>Estate Investing Strategy</li>
    </ul>

    <div class="cta">
      <span class="cta__label">Get Started</span>
      <svg class="cta__icon" viewBox="0 0 32 32" aria-hidden="true">
        <circle cx="16" cy="16" r="15" fill="var(--button-ink)"/>
        <path d="M12.5 9.5 L22.5 16 L12.5 22.5 Z" fill="var(--white)"/>
      </svg>
    </div>
  </div>
</body>
</html>
```